Food home delivery flyer to attract new customers and drive web traffic

We need a flyer for Grubella Home Delivery for our door to door leaflet drop. The aim of our marketing is to attract new customers by driving traffic to our website and raise awareness of our service.

We want the flyer in A5, double sided, and in colour. This campaign will be primarily in print, but we need a PDF option also.

Please visit www.grubellahomedelivery.example to obtain a real feel of who we are and what we do.

The flyer should contain the Grubella Home Delivery logo, with our images to compliment our service and what we offer. All are attached to this brief, along with what wording we expect to be included in the flyer.

The main points we need to shout about are:
Sourcing fresh produce from local growers
Partnering with local businesses
Friendly team offering superior customer service
Fast, safe home delivery
Sustainable business

```html
<!DOCTYPE html>
<html lang="en">
<head>
<meta charset="utf-8">
<title>Grubella Home Delivery – A5 Flyer</title>
<link href="https://fonts.googleapis.com/css2?family=Montserrat:wght@400;500;600;700;800;900&display=swap" rel="stylesheet">
<style>
  :root {
    --green-dark: #1b6a33;
    --green-lime: #8dbb3a;
    --frame-grey: #6d6e70;
    --ink: #2b2b2b;
    --paper: #ffffff;
    --backdrop: #e6e7e8;
    --panel-veil: rgba(255,255,255,0.82);
  }
  * { box-sizing: border-box; margin: 0; padding: 0; }
  html, body { width: 1200px; height: 878px; overflow: hidden; }
  body {
    background: var(--backdrop);
    font-family: "Montserrat", Arial, sans-serif;
    color: var(--ink);
    position: relative;
  }
  .page {
    position: absolute;
    top: 86px;
    width: 498px;
    height: 706px;
    background: var(--paper);
    box-shadow: 0 2px 8px rgba(0,0,0,0.25);
    overflow: hidden;
  }
  .page--front { left: 86px; }
  .page--back { left: 615px; }

  /* Front */
  .front-header {
    position: absolute; left: 0; top: 0; width: 100%; height: 105px;
    background: var(--green-dark);
    display: flex; align-items: center; justify-content: center;
    text-align: center;
    color: #fff;
    font-weight: 800;
    font-size: 25px;
    line-height: 33px;
    letter-spacing: 0.3px;
    text-transform: uppercase;
  }
  .front-gallery {
    position: absolute; left: 0; top: 105px; width: 100%; height: 509px;
    background: var(--green-lime);
  }
  .tile {
    position: absolute;
    border: 3px solid var(--frame-grey);
  }
  .tile--pizza { left: 22px; top: 21px; width: 294px; height: 150px;
    background: linear-gradient(135deg, #c9572e, #e0893f 45%, #b8422a 75%, #6f5a3e); }
  .tile--logo { left: 22px; top: 180px; width: 294px; height: 150px; background: #fff;
    display: flex; align-items: center; justify-content: center; }
  .tile--veg { left: 22px; top: 340px; width: 294px; height: 150px;
    background: linear-gradient(120deg, #6c3f6a, #d9862b 30%, #5d9a34 55%, #c8322b 80%, #e5b93a); }
  .tile--platter { left: 326px; top: 21px; width: 150px; height: 229px;
    background: linear-gradient(160deg, #efe6da, #d9c2a4 40%, #c8402f 75%, #efe3d0); }
  .tile--picnic { left: 326px; top: 260px; width: 150px; height: 230px;
    background: linear-gradient(170deg, #c9a56a, #9c7a45 35%, #7ea33f 60%, #c57a3a 85%, #6b6a3c); }

  .brand {
    color: var(--green-dark);
    font-weight: 600;
    text-align: right;
    line-height: 1;
  }
  .brand__name { display: block; }
  .brand__tag { display: block; margin-top: 6px; }
  .brand--small .brand__name { font-size: 48px; letter-spacing: -1px; }
  .brand--small .brand__tag { font-size: 17px; }
  .brand--large .brand__name { font-size: 58px; letter-spacing: -1px; }
  .brand--large .brand__tag { font-size: 20px; }

  .page-footer {
    position: absolute; left: 0; bottom: 0; width: 100%; height: 92px;
    display: flex; flex-direction: column; align-items: center; justify-content: center;
    text-align: center;
    font-size: 13.6px;
    line-height: 17px;
    padding-bottom: 6px;
  }
  .page-footer strong { color: var(--green-dark); font-weight: 800; }

  /* Back */
  .back-brand-area {
    position: absolute; left: 0; top: 0; width: 100%; height: 166px;
    display: flex; align-items: center; justify-content: center;
  }
  .back-produce {
    position: absolute; left: 0; top: 166px; width: 100%; height: 443px;
    background: linear-gradient(120deg, #5c7a3a, #b8c77a 20%, #e9d27a 45%, #d98a5a 65%, #8f5a8a 85%, #c7cfa0);
    border-bottom: 4px solid var(--green-dark);
  }
  .info-panel {
    position: absolute; left: 17px; top: 18px; width: 464px; height: 421px;
    background: var(--panel-veil);
    border: 3px solid var(--frame-grey);
    border-bottom: none;
    text-align: center;
    padding: 26px 22px 0;
  }
  .info-panel h2 {
    color: var(--green-dark);
    font-weight: 800;
    font-size: 21px;
    letter-spacing: 0.2px;
    margin-bottom: 17px;
    text-transform: uppercase;
  }
  .info-panel p {
    font-size: 12.6px;
    line-height: 15.7px;
    margin-bottom: 15.5px;
  }
  .info-panel a { color: var(--green-dark); text-decoration: none; }
  .offer-tab {
    position: absolute; left: 83px; bottom: 0; width: 334px; height: 49px;
    background: var(--green-dark);
    border-radius: 36px 36px 0 0;
    color: #fff;
    text-align: center;
    font-size: 13px;
    line-height: 16px;
    padding-top: 8px;
  }
  .offer-tab strong { font-weight: 800; }
</style>
</head>
<body>

  <section class="page page--front">
    <header class="front-header">Sourcing fresh produce<br>from local growers</header>
    <div class="front-gallery">
      <div class="tile tile--pizza" role="img" aria-label="Photo of a tomato and basil pizza"></div>
      <div class="tile tile--platter" role="img" aria-label="Photo of a Mediterranean antipasti platter with bread, tomatoes and wine"></div>
      <div class="tile tile--logo">
        <div class="brand brand--small">
          <span class="brand__name">Grubella</span>
          <span class="brand__tag">home delivery</span>
        </div>
      </div>
      <div class="tile tile--picnic" role="img" aria-label="Photo of a handmade picnic spread with pies, scotch eggs and salad"></div>
      <div class="tile tile--veg" role="img" aria-label="Photo of a colourful pile of fresh vegetables and fruit"></div>
    </div>
    <footer class="page-footer">
      <span>Shop now at <strong>www.grubellahomedelivery.example</strong></span>
      <span>or call one of our friendly team at the farm on <strong>01632 960418.</strong></span>
      <span>Start enjoying food wit provenance now.</span>
    </footer>
  </section>

  <section class="page page--back">
    <div class="back-brand-area">
      <div class="brand brand--large">
        <span class="brand__name">Grubella</span>
        <span class="brand__tag">home delivery</span>
      </div>
    </div>
    <div class="back-produce" role="img" aria-label="Background photo of fresh mixed vegetables">
      <div class="info-panel">
        <h2>Fast, safe home delivery</h2>
        <p>Lovingly picked Kentish food safely delivered from our farm to your home by passionate local people who care.</p>
        <p>Avoid the supermarkets and enjoy a unique and balanced food experience with provenance. Order online at <a href="#">www.grubellahomedelivery.example</a> for fast contactless next day delivery.</p>
        <p>Grubella brings you the very best producers and growers from The Garden of England to deliver you a delicious choice for all your dining needs. From fresh produce boxes, handmade picnic boxes, fresh Kentish berry boxes to the finest local beer and wines–we’ve got it covered.</p>
        <p>Using environmentally consciouspractices and minimal packaging, working hand in hand with reduced food miles brings you peace of mind with our efforts for a sustainable future.</p>
        <div class="offer-tab">
          Enjoy <strong>25%</strong> off all your orders in <strong>July</strong><br>
          enter code <strong>LOCALGROWN</strong> at the checkout
        </div>
      </div>
    </div>
    <footer class="page-footer">
      <span>Shop now at <strong>www.grubellahomedelivery.example</strong></span>
      <span>or call one of our friendly team at the farm on <strong>01632 960418.</strong></span>
      <span>Start enjoying food wit provenance now.</span>
    </footer>
  </section>

</body>
</html>
```